RW Frameworks Inc Business cards

We need business cards using our existing logo but slightly modified. Right now the logo says RW Framework Masonry. We want to keep the RW part of the design, but replace the Framework Masonry portion with "FRAMEWORKS". Please see the attached file.
Ideally this would be a blank template so we can add Different Names, titles, and phone numbers later.
On the one side we want only the logo and on the other side the detail. I'm attaching an example for you to see.
Please reach out with any other questions. Our address and other details will be given out once we find a design we like.

Target Market(s)

Construction Industry

```html
<!DOCTYPE html>
<html lang="en">
<head>
<meta charset="utf-8">
<title>RW Frameworks Inc – Business Cards</title>
<link rel="stylesheet" href="https://fonts.googleapis.com/css2?family=Montserrat:wght@400;500;600;700&display=swap">
<style>
  :root {
    --canvas-bg: #dedede;
    --front-blue: #1a5f93;
    --logo-light: #a9cfea;
    --brand-blue: #1872b8;
    --back-bg: #f4f4fa;
    --sketch-tone: #e9ebf2;
    --title-grey: #555555;
    --body-text: #2b2b2b;
  }
  * { margin: 0; padding: 0; box-sizing: border-box; }
  html, body { width: 1200px; height: 1200px; overflow: hidden; }
  body {
    background: var(--canvas-bg);
    font-family: "Montserrat", Arial, sans-serif;
    position: relative;
  }
  .card {
    position: absolute;
    left: 182px;
    width: 833px;
    height: 472px;
    overflow: hidden;
  }
  .card-front { top: 101px; background: var(--front-blue); }
  .card-back { top: 616px; background: var(--back-bg); }

  .wordmark-initials,
  .wordmark-name {
    position: absolute;
    display: block;
    text-align: center;
    font-weight: 600;
    line-height: 1;
    white-space: nowrap;
  }
  .card-front .wordmark { color: var(--logo-light); }
  .card-front .wordmark-initials {
    left: 0; width: 833px; top: 118px;
    font-size: 170px; letter-spacing: 4px;
  }
  .card-front .wordmark-name {
    left: 0; width: 833px; top: 277px;
    font-size: 42px; letter-spacing: 5px;
  }

  .sketch-area {
    position: absolute;
    left: 0; top: 0;
    width: 833px; height: 472px;
    background: linear-gradient(100deg, var(--sketch-tone) 0%, var(--sketch-tone) 30%, rgba(244,244,250,0) 60%);
  }
  .card-back .wordmark { color: var(--brand-blue); }
  .card-back .wordmark-initials {
    left: 118px; width: 240px; top: 154px;
    font-size: 118px; letter-spacing: 3px;
  }
  .card-back .wordmark-name {
    left: 118px; width: 240px; top: 264px;
    font-size: 30px; letter-spacing: 3px;
  }

  .details { position: absolute; left: 455px; top: 78px; width: 300px; }
  .person-name { font-size: 33px; font-weight: 700; color: var(--brand-blue); }
  .person-title { font-size: 22px; font-weight: 600; color: var(--title-grey); margin-top: 12px; }
  .divider { height: 2px; width: 292px; background: var(--brand-blue); margin-top: 18px; }
  .contact-list { list-style: none; margin-top: 26px; }
  .contact-item {
    display: flex; align-items: flex-start;
    font-size: 18px; color: var(--body-text);
    line-height: 25px; margin-bottom: 18px;
  }
  .contact-icon { width: 22px; height: 22px; margin-right: 14px; margin-left: -4px; flex: none; margin-top: 1px; fill: var(--brand-blue); }
</style>
</head>
<body>
  <section class="card card-front" aria-label="Card front">
    <div class="wordmark">
      <span class="wordmark-initials">RW</span>
      <span class="wordmark-name">Frameworks</span>
    </div>
  </section>

  <section class="card card-back" aria-label="Card back">
    <div class="sketch-area" role="img" aria-label="Faint architectural line sketch of a house in the background"></div>
    <div class="wordmark">
      <span class="wordmark-initials">RW</span>
      <span class="wordmark-name">Frameworks</span>
    </div>

    <div class="details">
      <h1 class="person-name">Alex Morgan</h1>
      <p class="person-title">Founder</p>
      <div class="divider"></div>
      <ul class="contact-list">
        <li class="contact-item">
          <svg class="contact-icon" viewBox="0 0 24 24" aria-hidden="true"><path d="M3 8c0-2 4-4 9-4s9 2 9 4v2h-5V8H8v2H3z"/><path d="M6 11h12l2 8H4z"/><circle cx="12" cy="15" r="2.2" fill="#f4f4fa"/></svg>
          <span>555-555-0148</span>
        </li>
        <li class="contact-item">
          <svg class="contact-icon" viewBox="0 0 24 24" aria-hidden="true"><path d="M12 2a7 7 0 0 0-7 7c0 5 7 13 7 13s7-8 7-13a7 7 0 0 0-7-7zm0 9.5A2.5 2.5 0 1 1 12 6.5a2.5 2.5 0 0 1 0 5z"/></svg>
          <span>sales@rwframeworks.com</span>
        </li>
        <li class="contact-item">
          <svg class="contact-icon" viewBox="0 0 24 24" aria-hidden="true"><path d="M2 6h20v13H2z"/><path d="M2 6l10 7 10-7" fill="none" stroke="#f4f4fa" stroke-width="1.8"/></svg>
          <span>www.rwframeworks.com</span>
        </li>
        <li class="contact-item">
          <svg class="contact-icon" viewBox="0 0 24 24" aria-hidden="true"><g fill="none" stroke="#1872b8" stroke-width="1.6"><circle cx="12" cy="12" r="9.5"/><ellipse cx="12" cy="12" rx="4.2" ry="9.5"/><path d="M2.5 12h19M4 7h16M4 17h16"/></g></svg>
          <span>214 Birchfield, Ridgeton,<br>ZZ 00000</span>
        </li>
      </ul>
    </div>
  </section>
</body>
</html>
```